Business Card Design

We need a new buisness card designed for a new company in Darwin
We dig trenchs and lay pipes for the communication industry,Electrical industry, Teleco industry,
We also do some concrete works as well,
And small excavation work
Communication
Belvanti Contracting PTY LTD
Pit and Pipe installations
Trenching,Excavations, Concreting ,
civil works, unistrut soloutions ,over thirty years experiance
WHERE NOT FAZED WE WILL LAY ANYTHING
Contact Glen 0491536208 ps
(would like name to stand out somehow in another text or graphic sort of a way am also looking for some sort of slogan) will most likely be a red card with black writing

```html
<!DOCTYPE html>
<html lang="en">
<head>
<meta charset="utf-8">
<title>Belvanti Contracting – Business Card</title>
<link rel="stylesheet" href="https://fonts.googleapis.com/css2?family=Roboto+Condensed:wght@700&family=Arimo:wght@700&family=Roboto:wght@300&display=swap">
<style>
  :root {
    --backdrop-centre: #5a5a5c;
    --backdrop-edge: #0e0e0e;
    --header-top: #e2e3e4;
    --header-bottom: #f6f7f7;
    --ink-grey: #4d4e50;
    --band-grey: #58595b;
    --accent-red: #b4121b;
    --footer-red-top: #cc2029;
    --footer-red-bottom: #5c0a0e;
    --white: #ffffff;
  }
  * { margin: 0; padding: 0; box-sizing: border-box; }
  html, body { width: 1200px; height: 999px; overflow: hidden; }
  body {
    position: relative;
    background: radial-gradient(ellipse 75% 80% at 50% 50%, var(--backdrop-centre) 0%, #3a3a3b 60%, var(--backdrop-edge) 100%);
  }
  .card {
    position: absolute;
    left: 75px; top: 199px;
    width: 1050px; height: 600px;
    overflow: visible;
  }
  .card-header {
    position: absolute; left: 0; top: 0;
    width: 100%; height: 229px;
    background: linear-gradient(to bottom, var(--header-top), var(--header-bottom) 45%);
    text-align: center;
  }
  .company-name {
    position: absolute; left: 0; right: 0; top: 36px;
    font-family: "Roboto Condensed", "Arial Narrow", sans-serif;
    font-weight: 700;
    font-size: 78px;
    line-height: 1;
    color: var(--ink-grey);
    white-space: nowrap;
  }
  .company-suffix { font-size: 34px; margin-left: 6px; }
  .slogan {
    position: absolute; left: 0; right: 0; top: 146px;
    font-family: "Arimo", Arial, sans-serif;
    font-weight: 700;
    font-size: 35px;
    color: var(--ink-grey);
    white-space: nowrap;
  }
  .divider {
    position: absolute; left: 0; top: 226px;
    width: 1050px; height: 32px;
  }
  .contact-band {
    position: absolute; left: 0; top: 239px;
    width: 100%; height: 251px;
    background: var(--band-grey);
    text-align: center;
    color: var(--white);
  }
  .contact-name {
    position: absolute; left: 0; right: 0; top: 60px;
    font-family: "Roboto Condensed", "Arial Narrow", sans-serif;
    font-weight: 700;
    font-size: 70px;
    line-height: 1;
  }
  .contact-phone {
    position: absolute; left: 0; right: 0; top: 150px;
    font-family: "Arimo", Arial, sans-serif;
    font-weight: 700;
    font-size: 60px;
    line-height: 1;
  }
  .services {
    position: absolute; left: 0; top: 490px;
    width: 100%; height: 110px;
    background: linear-gradient(to bottom, var(--footer-red-top), #a0141b 45%, var(--footer-red-bottom));
    color: var(--white);
    text-align: center;
    font-family: "Roboto", Arial, sans-serif;
    font-weight: 300;
    font-size: 28px;
    line-height: 38px;
    padding-top: 8px;
  }
  .contact-band, .divider { z-index: 1; }
  .divider { z-index: 2; }
</style>
</head>
<body>
  <section class="card">
    <header class="card-header">
      <h1 class="company-name">BELVANTI CONTRACTING<span class="company-suffix">PTY LTD</span></h1>
      <p class="slogan">WHERE NOT FAZED WE WILL LAY ANYTHING</p>
    </header>
    <svg class="divider" viewBox="0 0 1050 32" aria-hidden="true">
      <rect x="0" y="2" width="1050" height="11" fill="var(--accent-red)"/>
      <polygon points="126,12 158,12 142,28" fill="var(--accent-red)"/>
    </svg>
    <div class="contact-band">
      <p class="contact-name">Glen</p>
      <p class="contact-phone">0491536208</p>
    </div>
    <footer class="services">
      <p>Pit and Pipe installations Trenching,Excavations, concreting civil works,</p>
      <p>over thirty years experiance</p>
    </footer>
  </section>
</body>
</html>
```